Monument sign* - Law Firm

*I am installing a monument sign that has LED, as well as backlit elements. I am seeking help in designing the backlit portion of the sign. The Backlit sign will be 12’ x 4’.

We are looking for a classic, yet eye-catching sign to help new and current clients find our firm as well as bring in future clients. One of our goals is that people who drive by on a regular basis remember our sign (and us) for any future legal need.

Target Market(s)

Current and future clientele

Industry/Entity Type

Law Firm

Font styles to use
Serif
Sans Serif

Colors
b1b1b1
333333

Requirements
Must have
• Business name: Hargrove Law Firm, Inc.
• Website: www.hargrovelawfirm-example.com
• Telephone: (555)214-3679
• Our firm's logo
Nice to have
• Color preference is black, taupe, and white. A photo for reference of the office coloring is uploaded.
• We currently have an established logo which our firm has been using for more than 10 years. Our logo has been used in advertising, commercials, letterhead, and on-site. We are looking to transition from brown/rust/cream to the black/taupe/white color scheme.
Should not have
• Cheesy slogans; character designs; directions; additional symbols outside of the firm's logo.

```html
<!DOCTYPE html>
<html lang="en">
<head>
<meta charset="utf-8">
<title>Hargrove Law Firm, Inc. – Monument Sign Face</title>
<link rel="stylesheet" href="https://fonts.googleapis.com/css2?family=Roboto+Condensed:wght@400&display=swap">
<style>
  :root {
    --backdrop: #e6e2dd;
    --frame-white: #ffffff;
    --panel-taupe: #c2c2c4;
    --ink: #4f4f52;
    --logo-dark: #3b2f28;
    --frame-shadow: rgba(0, 0, 0, 0.18);
  }
  html, body {
    margin: 0;
    padding: 0;
    width: 1200px;
    height: 676px;
    overflow: hidden;
    background: var(--backdrop);
  }
  .canvas {
    position: relative;
    width: 1200px;
    height: 676px;
  }
  .sign-face {
    position: absolute;
    left: 50px;
    top: 155px;
    width: 1100px;
    height: 366px;
    background: var(--frame-white);
    box-shadow: 0 6px 22px var(--frame-shadow);
  }
  .sign-panel {
    position: absolute;
    left: 24px;
    top: 22px;
    right: 24px;
    bottom: 22px;
    background: var(--panel-taupe);
  }
  .firm-mark {
    position: absolute;
    left: 18px;
    top: 18px;
    width: 210px;
    height: 190px;
  }
  .firm-mark__square {
    position: absolute;
    left: 0;
    top: 0;
    width: 160px;
    height: 160px;
    background: var(--logo-dark);
  }
  .firm-mark__name {
    position: absolute;
    left: 168px;
    top: 0;
    width: 160px;
    height: 30px;
    transform-origin: 0 0;
    transform: translate(30px, 0) rotate(90deg);
    font-family: "Roboto Condensed", sans-serif;
    font-weight: 400;
    font-size: 19px;
    letter-spacing: 2px;
    line-height: 30px;
    color: var(--logo-dark);
    white-space: nowrap;
    text-transform: uppercase;
  }
  .firm-info {
    position: absolute;
    left: 250px;
    right: 20px;
    top: 48px;
    font-family: "Roboto Condensed", sans-serif;
    font-weight: 400;
    color: var(--ink);
  }
  .firm-info__name {
    margin: 0;
    font-size: 74px;
    line-height: 1;
    letter-spacing: -0.5px;
    text-align: center;
    font-weight: 400;
  }
  .firm-info__contacts {
    list-style: none;
    margin: 26px 0 0 0;
    padding: 0;
    display: flex;
    flex-direction: column;
    align-items: center;
    gap: 6px;
    font-size: 26px;
  }
  .contact-line {
    display: flex;
    align-items: center;
    gap: 10px;
  }
  .contact-line__icon {
    width: 20px;
    height: 20px;
    flex: none;
  }
</style>
</head>
<body>
<main class="canvas">
  <section class="sign-face" aria-label="Backlit sign face">
    <div class="sign-panel">
      <div class="firm-mark">
        <div class="firm-mark__square"></div>
        <div class="firm-mark__name">Hargrove Law Firm</div>
      </div>
      <div class="firm-info">
        <h1 class="firm-info__name">Hargrove Law Firm, Inc.</h1>
        <ul class="firm-info__contacts">
          <li class="contact-line">
            <svg class="contact-line__icon" viewBox="0 0 20 20" aria-hidden="true">
              <g fill="none" stroke="#4f4f52" stroke-width="1.6">
                <circle cx="10" cy="10" r="8.2"/>
                <ellipse cx="10" cy="10" rx="3.6" ry="8.2"/>
                <line x1="1.8" y1="10" x2="18.2" y2="10"/>
                <path d="M3.3 5.6 H16.7 M3.3 14.4 H16.7"/>
              </g>
            </svg>
            <span>www.hargrovelawfirm-example.com</span>
          </li>
          <li class="contact-line">
            <svg class="contact-line__icon" viewBox="0 0 20 20" aria-hidden="true">
              <path d="M4.2 2.5 L7.2 2.2 L8.6 6.4 L6.7 7.8 C7.6 9.9 9.9 12.3 12.2 13.3 L13.6 11.4 L17.8 12.8 L17.5 15.8 C17.3 17 16.3 17.8 15.1 17.7 C8.5 17.1 2.9 11.5 2.3 4.9 C2.2 3.7 3 2.7 4.2 2.5 Z" fill="none" stroke="#4f4f52" stroke-width="1.6" stroke-linejoin="round"/>
              <path d="M11.5 3.2 A5.3 5.3 0 0 1 16.8 8.5 M11.3 6 A2.5 2.5 0 0 1 14 8.7" fill="none" stroke="#4f4f52" stroke-width="1.4" stroke-linecap="round"/>
            </svg>
            <span>(555)214-3679</span>
          </li>
        </ul>
      </div>
    </div>
  </section>
</main>
</body>
</html>
```